LOOP 20th Anniversary Letterhead

LOOP – Guidance, Reach, and Insight – is Harbor Works’s premiere Frontline Associate training program. LOOP includes compliance training, professional development, skill building, and training for corporate and sector-specific initiatives for all Harbor Works Frontline Associates.

We are celebrating our 20th anniversary in 2017! We would like our letterhead and logo to include some nod to this 20th anniversary. We're open to ideas that showcases this great milestone for the program. We will use this letterhead to showcase our anniversary in multiple training and marketing mediums throughout the year.

Logo: We would like to include our current logo with something to call out our 20th anniversary; we won't need a totally new logo from scratch. This logo should go at the top of the letterhead. We will need to include the Harbor Works/Onward Bright logo in the footer of the letterhead. It can be smaller though.

Letterhead: This letterhead will be used both in portrait and landscape on 8 1/2 X 11 paper. Often we use this letterhead in PowerPoint for slides, as well as in a lesson plan. We need to include enough space write a title in the header.

We are open to a watermark, but would love to see letterheads with and without it.

I have included our current template and two logos (that should be used).
Updates

Project Deadline Extended
Reason: We would like to extend the deadline for this project to allow for more submissions and/or revision to current submissions. We are most interested in designs that include something about our 20th anniversary (1997 - 2017) in either our logo, the header/footer, or in a watermark.

Target Market(s)

Frontline Associates (hourly associates), Managers

Industry/Entity Type

Communication

Logo Text

LOOP 20th Anniversary

Font styles to use
Other font styles liked:
• Calibri; Century Gothic

Colors
6b449b
000000
cbcbcb

Requirements
Must have
• - Appropriate for web and print
• - EPS, JPEG, PNG
• - Purple (from the LOOP logo), black, and gray color scheme
• - Transparent
• - Space to put a title in the header
• - No more than 1 inch from the top
• - Portrait and Landscape to use on letterhead and PowerPoint
Nice to have
• - Maybe a watermark? <-- We are open to seeing designs with and without it.
• - Should look good when printed in color or black and white
Should not have
• - No stock images, clip art
• - Overly large graphics that take up too much space in the body of the letterhead. We will need to create text here.

```html
<!DOCTYPE html>
<html lang="en">
<head>
<meta charset="utf-8">
<title>LOOP 20th Anniversary Letterhead</title>
<link href="https://fonts.googleapis.com/css2?family=Arimo:wght@400;700&family=Questrial&display=swap" rel="stylesheet">
<style>
  :root {
    --purple: #4a2d8c;
    --charcoal: #3a3a3c;
    --ink: #1c1c1c;
    --grey: #cbcbcb;
    --lavender: #d3d0e3;
    --backdrop: #ececec;
    --paper: #f7f7f7;
  }
  * { margin: 0; padding: 0; box-sizing: border-box; }
  html, body { width: 1200px; height: 795px; overflow: hidden; }
  body {
    background: var(--backdrop);
    font-family: "Arimo", Arial, sans-serif;
    color: var(--ink);
    position: relative;
  }
  .letterhead {
    position: absolute;
    left: 320px; top: 35px;
    width: 560px; height: 725px;
    background: var(--paper);
    box-shadow: 0 2px 10px rgba(0,0,0,0.12);
    overflow: hidden;
  }
  .corner-stripes { position: absolute; left: 0; top: 0; width: 560px; height: 725px; }

  .brand { position: absolute; left: 58px; top: 66px; display: flex; align-items: center; gap: 8px; }
  .brand-square { width: 14px; height: 14px; background: var(--purple); }
  .brand-name { font-family: "Questrial", "Century Gothic", sans-serif; font-size: 34px; color: var(--purple); letter-spacing: 2px; line-height: 1; }
  .brand-tagline { position: absolute; left: 58px; top: 106px; font-size: 7px; letter-spacing: 1.2px; text-transform: uppercase; color: var(--ink); }

  .contact {
    position: absolute; left: 400px; top: 56px;
    border-left: 1px solid var(--purple);
    padding-left: 8px;
    font-size: 7px; line-height: 10px; color: var(--ink);
  }
  .contact .row { display: flex; align-items: center; gap: 4px; }
  .contact svg { width: 7px; height: 7px; fill: var(--purple); }
  .contact .web { color: var(--purple); }

  .recipient { position: absolute; left: 58px; top: 170px; font-size: 8.5px; line-height: 11px; }
  .recipient .name { font-weight: 700; font-size: 9px; }

  .letter-body { position: absolute; left: 100px; top: 236px; width: 400px; font-size: 8.5px; line-height: 13px; }
  .letter-body p { margin-bottom: 13px; }

  .signature { position: absolute; left: 150px; top: 520px; width: 120px; height: 36px; background: #e2e2e2; }
  .signer { position: absolute; left: 150px; top: 564px; font-size: 8.5px; line-height: 11px; }
  .signer .title { font-weight: 700; }

  .anniversary { position: absolute; right: 40px; top: 520px; text-align: right; color: var(--lavender); font-family: "Questrial", "Century Gothic", sans-serif; }
  .anniversary .years { font-size: 72px; line-height: 0.9; letter-spacing: -1px; }
  .anniversary .word { font-size: 22px; letter-spacing: 1px; }

  .partners { position: absolute; left: 240px; top: 664px; display: flex; align-items: center; gap: 8px; font-size: 9px; }
  .partners .harbor { letter-spacing: 1.5px; text-transform: uppercase; color: var(--ink); }
  .partners .divider { width: 1px; height: 12px; background: var(--ink); }
  .partners .onward { font-weight: 700; color: var(--ink); }
</style>
</head>
<body>
  <main class="letterhead">
    <svg class="corner-stripes" viewBox="0 0 560 725" aria-hidden="true">
      <polygon points="200,708 560,646 560,661" fill="var(--charcoal)"/>
      <polygon points="130,725 560,668 560,725" fill="var(--purple)"/>
    </svg>

    <div class="brand">
      <span class="brand-name">LOOP</span>
      <span class="brand-square"></span>
    </div>
    <div class="brand-tagline">Guidance, Reach, and Insight</div>

    <address class="contact">
      <div>PO BOX 480 Linden Row</div>
      <div>7th street Fairhaven</div>
      <div class="row"><svg viewBox="0 0 10 10"><path d="M2 1h2l1 2.5-1.2 1a5 5 0 0 0 2.7 2.7l1-1.2L10 7v2c0 .6-.4 1-1 1A9 9 0 0 1 0 1c0-.6.4-1 1-1z"/></svg>(02)4815 162 342</div>
      <div class="row"><svg viewBox="0 0 10 10"><rect x="1" y="3" width="8" height="6"/><rect x="3" y="0" width="4" height="3"/></svg>(02)4815 162 343</div>
      <div class="web">www.loopprogram.org</div>
    </address>

    <div class="recipient">
      <div class="name">MARA QUILL</div>
      <div>Street Name City Name.</div>
      <div>Zip Coad 0000</div>
    </div>

    <section class="letter-body">
      <p>Lorem Ipsum is simply dummy text of the printing and typesetting industry. Lorem Ipsum has been the industry's standard dummy text ever since the 1500s, when an unknown printer took a galley of type and scrambled it to make a type specimen book. It has survived not only five centuries, but also the leap into electronic typesetting, remaining essentially unchanged. It was popularised in the 1960s with the release of Fontmark sheets containing Lorem Ipsum passages, and more recently with desktop publishing software like Pagewright including versions of Lorem Ipsum.</p>
      <p>It is a long established fact that a reader will be distracted by the readable content of a page when looking at its layout. The point of using Lorem Ipsum is that it has a more-or-less normal distribution of letters, as opposed to using 'Content here, content here', making it look like readable English. Many desktop and publishing packages and web page editors now use Lorem Ipsum as their default model text, and a search for 'lorem ipsum' will uncover many web sites still in their infancy. Various versions have evolved over the years, sometimes by accident, sometimes on purpose (injected humour and the like).</p>
      <p>Regards,</p>
    </section>

    <div class="signature" role="img" aria-label="Handwritten signature of Elias Vennor"></div>
    <div class="signer">
      <div>Elias Vennor</div>
      <div class="title">General Manager</div>
    </div>

    <div class="anniversary">
      <div class="years">20th</div>
      <div class="word">anniversary</div>
    </div>

    <div class="partners">
      <span class="harbor">Harbor Works</span>
      <span class="divider"></span>
      <span class="onward">Onward Bright</span>
    </div>
  </main>
</body>
</html>
```